Business Card for New Business

Please design a business card using our logo and font files. This is only one card for one person, as listed in details section.

Industry/Entity Type

Business

Contact Information for Business Card

Carl Voserby

Phone 240.318.6624
Cell 703.581.4096
Email carl@moltravex.com

www.moltravex.com

Address
18250 Brennick Lane #314
Kellsmoor, NV 20715

Font styles to use
Sans Serif

Requirements
Must have
• Information listed in detail section. Must be standard card size.

```html
<!DOCTYPE html>
<html lang="en">
<head>
<meta charset="utf-8">
<title>Moltravex – Business Card</title>
<link rel="stylesheet" href="https://fonts.googleapis.com/css2?family=Josefin+Sans:wght@600;700&family=Quicksand:wght@300;400&display=swap">
<style>
  :root {
    --page-bg: #dfe4ea;
    --card-bg: #f1f2f4;
    --brand-red: #8f1f1a;
    --band-red: #a0443e;
    --circle-red: #a9524d;
    --ink-dark: #2b2b2e;
    --contact-ink: #ead8da;
    --icon-bg: #3b3f4a;
    --divider: #9a3a30;
    --tab-edge: #c9cdd4;
  }
  * { box-sizing: border-box; margin: 0; padding: 0; }
  html, body { width: 1200px; height: 900px; overflow: hidden; }
  body { background: var(--page-bg); position: relative; }

  .business-card {
    position: absolute;
    left: 150px; top: 194px;
    width: 900px; height: 514px;
    background: var(--card-bg);
    box-shadow: 0 10px 30px rgba(0,0,0,0.12);
    overflow: hidden;
  }
  .card-shapes { position: absolute; inset: 0; }

  .brand-name {
    position: absolute;
    left: 55px; top: 108px;
    font-family: "Quicksand", sans-serif;
    font-weight: 400;
    font-size: 50px;
    letter-spacing: 1px;
    color: var(--brand-red);
    display: flex; align-items: center; gap: 12px;
  }
  .brand-dot {
    width: 30px; height: 30px; border-radius: 50%;
    background: var(--brand-red);
  }

  .divider {
    position: absolute; left: 414px; top: 90px;
    width: 2px; height: 132px; background: var(--divider);
  }

  .person-name {
    position: absolute; left: 470px; top: 118px;
    font-family: "Josefin Sans", sans-serif;
    font-weight: 600; font-size: 32px; color: var(--ink-dark);
  }
  .person-role {
    position: absolute; left: 470px; top: 172px;
    font-family: "Josefin Sans", sans-serif;
    font-weight: 700; font-size: 17px; color: var(--ink-dark);
  }

  .contact-list {
    position: absolute; left: 440px; top: 300px;
    list-style: none;
    font-family: "Quicksand", sans-serif;
    font-weight: 300; font-size: 27px; color: var(--contact-ink);
  }
  .contact-list li { display: flex; align-items: center; height: 36px; white-space: nowrap; }
  .contact-list .icon { width: 22px; height: 22px; margin-right: 10px; flex: none; }
  .contact-list .address-line { padding-left: 32px; }

  .website {
    position: absolute; left: 52px; top: 464px;
    font-family: "Quicksand", sans-serif;
    font-weight: 400; font-size: 27px; color: var(--contact-ink);
    white-space: nowrap;
  }
</style>
</head>
<body>
  <div class="business-card">
    <svg class="card-shapes" width="900" height="514" viewBox="0 0 900 514">
      <circle class="accent-circle" cx="202" cy="328" r="98" fill="var(--circle-red)"/>
      <path class="contact-band" d="M338 514 L338 390 Q338 242 500 242 L900 242 L900 514 Z" fill="var(--band-red)"/>
      <path class="web-tab" d="M0 450 L380 450 Q432 450 432 500 L432 514 L0 514 Z" fill="var(--band-red)"/>
      <path class="web-tab-edge" d="M380 450 Q432 450 432 500 L432 514" fill="none" stroke="var(--tab-edge)" stroke-width="4"/>
    </svg>

    <div class="brand-name"><span class="brand-dot"></span>moltravex</div>
    <div class="divider"></div>

    <div class="person-name">Carl Voserby</div>
    <div class="person-role">POSITION</div>

    <ul class="contact-list">
      <li>
        <svg class="icon" viewBox="0 0 20 20"><rect width="20" height="20" rx="5" fill="var(--icon-bg)"/><rect x="6.5" y="3.5" width="7" height="13" rx="1.5" fill="none" stroke="#fff" stroke-width="1.4"/><circle cx="10" cy="14" r="0.9" fill="#fff"/></svg>
        703.581.4096
      </li>
      <li>
        <svg class="icon" viewBox="0 0 20 20"><circle cx="10" cy="10" r="10" fill="var(--icon-bg)"/><path d="M4 9 Q10 4 16 9 L14.5 10.5 L12.5 9 L7.5 9 L5.5 10.5 Z" fill="#fff"/><rect x="6" y="11" width="8" height="4" rx="1" fill="#fff"/></svg>
        240.318.6624
      </li>
      <li>
        <svg class="icon" viewBox="0 0 20 20"><circle cx="10" cy="10" r="10" fill="var(--icon-bg)"/><rect x="4.5" y="6.5" width="11" height="8" fill="none" stroke="#fff" stroke-width="1.3"/><path d="M4.5 6.5 L10 11 L15.5 6.5" fill="none" stroke="#fff" stroke-width="1.3"/></svg>
        carl@moltravex.com
      </li>
      <li>
        <svg class="icon" viewBox="0 0 20 20"><circle cx="10" cy="10" r="10" fill="var(--icon-bg)"/><path d="M4 10 L10 4.5 L16 10 L14.5 10 L14.5 15 L11.5 15 L11.5 12 L8.5 12 L8.5 15 L5.5 15 L5.5 10 Z" fill="#fff"/></svg>
        18250 Brennick Lane #314
      </li>
      <li class="address-line">Kellsmoor, NV 20715</li>
    </ul>

    <div class="website">www.moltravex.com</div>
  </div>
</body>
</html>
```